Larkfield Medical Rooms - Websit, online payment facility and patient information portal

We are a small specialist medical centre inNewcastle NSW, Australia. We would like a modern, open easy to navigate (we have many elderly clients) webpage for our customers to use. We would like a page for content uploads (like referrals etc), an enquiry page, and some patient information pages.

Our logo is attached. We would like a modern, grey scale or black and white website for our customers to use. The landing page should have high resolution images and use san serif font.

Target Market(s)

General Audience, Modern

Industry/Entity Type

Health And Wellness

Coding

Coded - Design and coding required

Number of Pages Required

5+ page

Font styles to use
Sans Serif

Colors
cbcbcb
757575
7f7f7f
c4c4c4
85cae6
cee9f5
cfdfed

Requirements
Must have
• Landing Page
• Several Other pages for content upload
• Ability to do online payments
• Enquiry form
• Contact page
• Social Media Links

```html
<!DOCTYPE html>
<html lang="en">
<head>
<meta charset="utf-8">
<title>Larkfield Medical Rooms</title>
<link href="https://fonts.googleapis.com/css2?family=Roboto:wght@400;500&display=swap" rel="stylesheet">
<style>
:root{
  --blue:#5aaedb;
  --blue-soft:#79c0e4;
  --ink:#222;
  --text:#666;
  --card:#ededed;
  --line:#dcdcdc;
  --footer:#f4f4f4;
  --white:#fff;
  --dark:#1c1c1c;
}
*{box-sizing:border-box;margin:0;padding:0}
h1,h2,h3,h4{font-weight:400}
html,body{width:696px;height:1200px;overflow:hidden;background:var(--white)}
body{position:relative;font-family:"Roboto",Arial,sans-serif;color:var(--text)}
.abs{position:absolute}

/* header */
.brand{left:76px;top:42px;color:var(--ink);font-size:14px;font-weight:400;line-height:18px;white-space:nowrap}
.search{left:478px;top:18px;width:141px;height:25px;border:1px solid #c9c9c9;font-size:7px;color:#999;padding:8px 0 0 9px}
.search svg{position:absolute;right:6px;top:7px}
.nav{top:71px;font-size:7px;letter-spacing:.3px;color:#555}
.nav.active{color:var(--blue)}

/* hero */
.hero{left:0;top:97px;width:696px;height:259px;background:linear-gradient(100deg,#d8dde3 0%,#eef1f4 30%,#f7f8f9 55%,#c9d6e4 75%,#3f73b8 82%,#e6e9ec 92%)}
.hero-arrow{top:219px;width:15px;height:15px;border-radius:50%;background:#7a7a7a;opacity:.85}
.hero-arrow svg{display:block}
.quick{left:461px;top:120px;width:158px;height:213px;background:var(--blue);padding:13px 9px}
.quick h2{font-size:14px;font-weight:500;color:var(--white);margin-bottom:9px}
.field{background:var(--white);height:23px;margin-bottom:5px;font-size:6px;color:#777;padding:8px 9px}
.field.msg{height:56px}
.submit{display:inline-block;background:var(--dark);color:var(--white);font-size:7px;font-weight:500;padding:7px 9px;margin-top:1px}

/* welcome */
.welcome-title{left:0;width:696px;top:393px;text-align:center;color:var(--blue);font-size:16.5px}
.welcome-copy{left:76px;width:543px;top:416px;text-align:center;font-size:6.3px;line-height:11px}

/* service cards */
.service{top:480px;width:172px;height:138px;background:var(--card);text-align:center}
.service svg{margin-top:17px}
.service h3{font-size:10.5px;color:var(--ink);margin-top:4px}
.service p{font-size:5.8px;line-height:10px;margin:5px 10px 0}
.more-btn{display:inline-block;margin-top:8px;width:52px;height:20px;border:1px solid #bbb;background:var(--white);font-size:5.6px;line-height:18px;color:#555;letter-spacing:.3px}

/* news */
.news{left:0;top:666px;width:696px;height:231px;background:linear-gradient(90deg,#dfe9f0 0%,#f0f4f6 40%,#eef2f5 70%,#cfdfed 100%)}
.news-title{left:0;width:696px;top:701px;text-align:center;color:var(--blue);font-size:16px}
.news-card{top:731px;width:126px;height:127px;background:var(--white);padding:22px 13px 0;box-shadow:0 1px 2px rgba(0,0,0,.12)}
.news-card time{display:block;font-size:6.8px;color:var(--blue);margin-bottom:9px}
.news-card p{font-size:7px;line-height:11.2px;color:#444}
.news-card .more{display:block;margin-top:10px;font-size:5.4px;color:#333;font-weight:500}
.news-arrow{top:775px}

/* call to action */
.cta-title{left:0;width:696px;top:939px;text-align:center;font-size:11.5px;color:var(--ink)}
.cta-copy{left:76px;width:543px;top:961px;text-align:center;font-size:6.2px;line-height:10.5px}
.cta-btn{left:278px;top:989px;width:139px;height:25px;background:var(--blue-soft);color:var(--white);font-size:8px;font-weight:500;letter-spacing:.4px;display:flex;align-items:center;justify-content:center;gap:4px}

/* footer */
.footer{left:0;top:1061px;width:696px;height:139px;background:var(--footer)}
.footer-bar{left:0;top:1165px;width:696px;height:1px;background:var(--line)}
.foot-head{top:1087px;font-size:8px;color:var(--ink)}
.foot-item{font-size:6.2px;color:#333;display:flex;align-items:center;gap:6px}
.foot-link{font-size:6.2px;color:#333}
.social{top:1104px;width:16px;height:16px;border-radius:50%}
.copyright{left:0;width:696px;top:1178px;text-align:center;font-size:6.2px;color:#333}
</style>
</head>
<body>

<header>
  <div class="abs brand">Larkfield Medical Rooms</div>
  <div class="abs search">Search
    <svg width="10" height="10" viewBox="0 0 10 10"><circle cx="4" cy="4" r="3" fill="none" stroke="#5aaedb" stroke-width="1.4"/><line x1="6.3" y1="6.3" x2="9" y2="9" stroke="#5aaedb" stroke-width="1.4"/></svg>
  </div>
  <nav>
    <span class="abs nav active" style="left:382px">HOME</span>
    <span class="abs nav" style="left:424px">ABOUT US</span>
    <span class="abs nav" style="left:479px">SERVICES</span>
    <span class="abs nav" style="left:534px">NEWS</span>
    <span class="abs nav" style="left:574px">CONTACT US</span>
  </nav>
</header>

<section>
  <div class="abs hero" role="img" aria-label="Photo of a bright hospital corridor with nurses walking and a patient bed"></div>
  <div class="abs hero-arrow" style="left:15px"><svg width="15" height="15" viewBox="0 0 15 15"><path d="M8.5 4.5 5.5 7.5 8.5 10.5" fill="none" stroke="#fff" stroke-width="1.6"/></svg></div>
  <div class="abs hero-arrow" style="left:666px"><svg width="15" height="15" viewBox="0 0 15 15"><path d="M6.5 4.5 9.5 7.5 6.5 10.5" fill="none" stroke="#fff" stroke-width="1.6"/></svg></div>
  <form class="abs quick">
    <h2>Quick Contact</h2>
    <div class="field">Name</div>
    <div class="field">Email</div>
    <div class="field">Phone</div>
    <div class="field msg">Message</div>
    <span class="submit">SUBMIT</span>
  </form>
</section>

<section>
  <h1 class="abs welcome-title">Welcome to Larkfield Medical Rooms</h1>
  <p class="abs welcome-copy">Etiam congue orci sit amet ex auctor, in vulputate magna lacinia. Morbi semper justo ut neque aliquet dictum. Fusce hendrerit neque rutrum nisi tristique euismod. Phasellus id pulvinar ipsum. Etiam quis cursus lorem. Etiam tincidunt commodo odio ut fermentum. Ut egestas pellentesque neque, nec pellentesque lacus euismod lobortis. In congue gravida pharetra. Duis quis nulla non ligula venenatis imperdiet. Donec felis orci, aliquam in lacinia id, lobortis eu justo. Cras purus neque, semper at felis id, sagittis scelerisque magna. Etiam eu tortor enim. Nulla libero libero, mattis id ante at, vehicula porta augue. Etiam at tortor ex. Integer non consectetur enim.</p>

  <article class="abs service" style="left:77px">
    <svg width="18" height="18" viewBox="0 0 18 18"><rect x="1.5" y="3" width="15" height="13.5" fill="none" stroke="#111" stroke-width="1.4"/><rect x="1.5" y="3" width="15" height="3" fill="#111"/><line x1="5" y1="1" x2="5" y2="4" stroke="#111" stroke-width="1.4"/><line x1="13" y1="1" x2="13" y2="4" stroke="#111" stroke-width="1.4"/><g fill="#111"><rect x="4" y="8" width="2" height="2"/><rect x="8" y="8" width="2" height="2"/><rect x="12" y="8" width="2" height="2"/><rect x="4" y="12" width="2" height="2"/><rect x="8" y="12" width="2" height="2"/><rect x="12" y="12" width="2" height="2"/></g></svg>
    <h3>Appointments</h3>
    <p>Cras purus neque, semper at felis id, sagittis scelerisque magna. Etiam eu tortor enim. Nulla libero libero, mattis id ante , vehicula porta augue</p>
    <span class="more-btn">READ MORE</span>
  </article>
  <article class="abs service" style="left:262px">
    <svg width="20" height="18" viewBox="0 0 20 18"><path d="M1 5h12v10H1z M13 8h3.5l2.5 3v4h-6z" fill="#111"/><circle cx="5" cy="15.5" r="2" fill="#111" stroke="#ededed"/><circle cx="15" cy="15.5" r="2" fill="#111" stroke="#ededed"/><path d="M6 7h2v2h2v2H8v2H6v-2H4V9h2z" fill="#ededed"/></svg>
    <h3>Emergencies</h3>
    <p>Cras purus neque, semper at felis id, sagittis scelerisque magna. Etiam eu tortor enim. Nulla libero libero, mattis id ante , vehicula porta augue</p>
    <span class="more-btn">READ MORE</span>
  </article>
  <article class="abs service" style="left:446px">
    <svg width="18" height="18" viewBox="0 0 18 18"><path d="M3 1h8l4 4v12H3z" fill="none" stroke="#111" stroke-width="1.4"/><path d="M11 1v4h4" fill="none" stroke="#111" stroke-width="1.2"/><g stroke="#111" stroke-width="1.2"><line x1="6" y1="8" x2="12" y2="8"/><line x1="6" y1="11" x2="12" y2="11"/><line x1="6" y1="14" x2="12" y2="14"/></g></svg>
    <h3>Prescriptions</h3>
    <p>Cras purus neque, semper at felis id, sagittis scelerisque magna. Etiam eu tortor enim. Nulla libero libero, mattis id ante , vehicula porta augue</p>
    <span class="more-btn">READ MORE</span>
  </article>
</section>

<section>
  <div class="abs news" role="img" aria-label="Soft blurred photo of a clinic waiting area"></div>
  <h2 class="abs news-title">Latest news</h2>
  <svg class="abs news-arrow" style="left:14px" width="10" height="14" viewBox="0 0 10 14"><path d="M7 1 2 7l5 6" fill="none" stroke="#9aa" stroke-width="1.4"/></svg>
  <svg class="abs news-arrow" style="left:673px" width="10" height="14" viewBox="0 0 10 14"><path d="M3 1l5 6-5 6" fill="none" stroke="#9aa" stroke-width="1.4"/></svg>
  <article class="abs news-card" style="left:77px"><time>18 JANUARY, 2017</time><p>Mauris et venenatis tortor, ac viverra purus. Vivamus pulvi nar dignissim arcu et aliquet. Morbi finibus finibus turpis nec accumsan.</p><span class="more">MORE ➔</span></article>
  <article class="abs news-card" style="left:215px"><time>18 JANUARY, 2017</time><p>Mauris et venenatis tortor, ac viverra purus. Vivamus pulvi nar dignissim arcu et aliquet. Morbi finibus finibus turpis nec accumsan.</p><span class="more">MORE ➔</span></article>
  <article class="abs news-card" style="left:354px"><time>18 JANUARY, 2017</time><p>Mauris et venenatis tortor, ac viverra purus. Vivamus pulvi nar dignissim arcu et aliquet. Morbi finibus finibus turpis nec accumsan.</p><span class="more">MORE ➔</span></article>
  <article class="abs news-card" style="left:493px"><time>18 JANUARY, 2017</time><p>Mauris et venenatis tortor, ac viverra purus. Vivamus pulvi nar dignissim arcu et aliquet. Morbi finibus finibus turpis nec accumsan.</p><span class="more">MORE ➔</span></article>
</section>

<section>
  <h2 class="abs cta-title">Cras urna sapien, ultricies quis porta ultricies, tincidunt quis diam</h2>
  <p class="abs cta-copy">Etiam congue orci sit amet ex auctor, in vulputate magna lacinia. Morbi semper justo ut neque aliquet dictum. Fusce hendrerit neque rutrum nisi tristique euismod. Phasellus id pulvinar ipsum. Etiam quis cursus lorem. Etiam tincidunt commodo odio ut fermentum. Ut egestas pellentesque neque, nec pellentesque lacus euismod lobortis.</p>
  <div class="abs cta-btn"><svg width="8" height="8" viewBox="0 0 8 8"><circle cx="4" cy="4" r="4" fill="#fff"/><path d="M3 2l2 2-2 2" fill="none" stroke="#79c0e4" stroke-width="1.2"/></svg>BOOK AN APPOINTMENT</div>
</section>

<footer>
  <div class="abs footer"></div>
  <h4 class="abs foot-head" style="left:76px">Harwick East</h4>
  <div class="abs foot-item" style="left:76px;top:1104px">⚲<span>24 Building name, Street name, City - Zipcode</span></div>
  <div class="abs foot-item" style="left:76px;top:1118px">▯<span>555 010 2024</span></div>
  <div class="abs foot-item" style="left:76px;top:1132px">✉<span>info@larkfieldmedicalrooms.com</span></div>
  <h4 class="abs foot-head" style="left:252px">Australia</h4>
  <div class="abs foot-item" style="left:252px;top:1104px">⚲<span>24 Building name, Street name, City - Zipcode</span></div>
  <div class="abs foot-item" style="left:252px;top:1118px">▯<span>555 010 2024</span></div>
  <div class="abs foot-item" style="left:252px;top:1132px">✉<span>info@larkfieldmedicalrooms.com</span></div>
  <h4 class="abs foot-head" style="left:433px">Links</h4>
  <span class="abs foot-link" style="left:433px;top:1104px">Home</span>
  <span class="abs foot-link" style="left:433px;top:1118px">About Us</span>
  <span class="abs foot-link" style="left:433px;top:1132px">Services</span>
  <span class="abs foot-link" style="left:480px;top:1104px">News</span>
  <span class="abs foot-link" style="left:480px;top:1118px">Contact Us</span>
  <h4 class="abs foot-head" style="left:546px">Follow us on</h4>
  <span class="abs social" style="left:546px;background:#3b5998" aria-label="Social link"></span>
  <span class="abs social" style="left:565px;background:#2fa3e6" aria-label="Social link"></span>
  <span class="abs social" style="left:584px;background:#1a6fb0" aria-label="Social link"></span>
  <span class="abs social" style="left:603px;background:#e0322a" aria-label="Social link"></span>
  <div class="abs footer-bar"></div>
  <p class="abs copyright">Copyright © 2017 Company name. All rights reserved.</p>
</footer>

</body>
</html>
```